International Company needs a Letterhead & Envelope Design

Our Company name is Brightfold Harbor Limited.
We'd like to ask the Designers for the luxurious and sophisticated design. Our logo is very simple and neat with letter logos, so we look forward to more professional and refined designs from Designers.
We look forward to providing you with a great design.
Thanks very much in advance.

```html
<!DOCTYPE html>
<html lang="en">
<head>
<meta charset="utf-8">
<title>Brightfold Harbor Limited – Letterhead &amp; Envelope</title>
<link href="https://fonts.googleapis.com/css2?family=Open+Sans:wght@400;600;700&display=swap" rel="stylesheet">
<style>
  :root{
    --stage:#e4e4e4;
    --paper:#ffffff;
    --ink:#1b1b1b;
    --brand-grey:#58595b;
    --accent-grey:#6d6e70;
    --black:#000000;
  }
  *{box-sizing:border-box;margin:0;padding:0}
  html,body{width:1200px;height:800px;overflow:hidden}
  body{background:var(--stage);font-family:"Open Sans",Arial,sans-serif;color:var(--ink);position:relative}

  .sheet{position:absolute;background:var(--paper);overflow:hidden}
  .side-bar{position:absolute;background:var(--black);width:14px}
  .brand-name{position:absolute;left:0;right:0;text-align:center;font-weight:700;color:var(--brand-grey);letter-spacing:1px;white-space:nowrap}

  /* Letterhead */
  .letterhead{left:13px;top:5px;width:579px;height:755px}
  .letterhead .side-bar{top:19px;height:72px}
  .letterhead .brand-name{top:40px;font-size:30px}
  .letter-body{position:absolute;left:53px;top:241px;width:486px;font-size:9.6px;line-height:11.5px}
  .letter-body p{margin-bottom:11.5px;text-align:justify}
  .letter-body .signature{margin-bottom:0}

  .contact-row{position:absolute;left:0;right:0;display:flex;justify-content:center;gap:34px;font-size:9.6px;white-space:nowrap}
  .contact-row span{display:flex;align-items:center;gap:5px}
  .contact-row svg{width:8px;height:8px}
  .address{position:absolute;left:0;right:0;text-align:center;font-size:9.6px;white-space:nowrap}
  .footer-stripes{position:absolute;left:0;bottom:0;width:100%}

  .letterhead .contact-row{top:695px;padding-left:0}
  .letterhead .address{top:710px}

  /* Envelope front */
  .envelope-front{left:605px;top:242px;width:565px;height:251px}
  .envelope-front .side-bar{top:18px;height:65px}
  .envelope-front .brand-name{top:33px;font-size:28px}
  .envelope-front .contact-row{top:195px}
  .envelope-front .address{top:209px}

  /* Envelope back */
  .envelope-back{left:603px;top:504px;width:567px;height:258px}
  .envelope-flap{position:absolute;left:0;top:0;width:100%;height:78px}
  .envelope-back .brand-name{top:23px;font-size:28px;color:var(--accent-grey)}
</style>
</head>
<body>

<section class="sheet letterhead" aria-label="Letterhead">
  <div class="side-bar" style="left:0"></div>
  <div class="side-bar" style="right:0"></div>
  <div class="brand-name">Brightfold Harbor Limited</div>

  <div class="letter-body">
    <p>Dear Mr. Smith,</p>
    <p>Lorem ipsum dolor sit amet, consectetuer adipiscing elit, sed diam nonummy nibh euismod tincidunt ut laoreet dolore magna aliquam erat volutpat. Ut wisi enim ad minim veniam, quis nostrud exerci tation ullamcorper suscipit lobortis nisl ut aliquip ex ea commodo consequat. Duis autem vel eum iriure dolor in hendrerit in vulputate velit esse molestie consequat,</p>
    <p>Lorem ipsum dolor sit amet, consectetuer adipiscing elit, sed diam nonummy nibh euismod tincidunt ut laoreet dolore magna aliquam erat volutpat. Ut wisi enim ad minim veniam, quis nostrud exerci tation ullamcorper suscipit lobortis nisl ut aliquip ex ea commodo consequat. Duis autem vel eum iriure dolor in hendrerit in vulputate velit esse molestie consequat, vel illum dolore eu feugiat nulla facilisis at vero eros et accumsan et iusto odio dignissim qui blandit praesent luptatum zzril delenit augue duis dolore te feugait nulla facilisi. Nam liber tempor cum soluta nobis eleifend option congue nihil imperdiet doming id quod mazim placerat facer possim assum.,</p>
    <p>Lorem ipsum dolor sit amet, consectetuer adipiscing elit, sed diam nonummy nibh euismod tincidunt ut laoreet dolore magna aliquam erat volutpat. Ut wisi enim ad minim veniam, quis nostrud exerci tation ullamcorper suscipit lobortis nisl ut aliquip ex ea commodo consequat. Duis autem vel eum iriure dolor in hendrerit in vulputate velit esse molestie consequat,</p>
    <p>Sincerely,</p>
    <p class="signature">John Doe<br>Sales Manager</p>
  </div>

  <div class="contact-row">
    <span><svg viewBox="0 0 10 10"><circle cx="5" cy="5" r="4.3" fill="none" stroke="#333" stroke-width="1"/><path d="M3.4 3 l1 1 -0.5 0.6 a3 3 0 0 0 1.5 1.5 l0.6-0.5 1 1 -0.7 0.8 C4.8 7.2 2.8 5.2 2.6 3.7z" fill="#333"/></svg>+0 123 456 789</span>
    <span><svg viewBox="0 0 10 10"><circle cx="5" cy="5" r="4.5" fill="#333"/><rect x="2.8" y="3.4" width="4.4" height="3.2" fill="#fff"/><path d="M2.8 3.4 L5 5.2 7.2 3.4" fill="none" stroke="#333" stroke-width="0.6"/></svg>info@yourmail.com</span>
    <span><svg viewBox="0 0 10 10"><circle cx="5" cy="5" r="4.5" fill="#555"/><circle cx="5" cy="5" r="2.4" fill="none" stroke="#ccc" stroke-width="0.7"/></svg>www.yourcompany.com</span>
  </div>
  <div class="address">Your address, Suit # 000, Dummy Street, City, State,</div>

  <svg class="footer-stripes" viewBox="0 0 579 28" height="28" preserveAspectRatio="none">
    <rect x="0" y="0" width="579" height="3.5" fill="#000"/>
    <polygon points="176,4 402,4 406,8 180,8" fill="#6d6e70"/>
    <rect x="0" y="8" width="579" height="20" fill="#000"/>
  </svg>
</section>

<section class="sheet envelope-front" aria-label="Envelope front">
  <div class="side-bar" style="left:0"></div>
  <div class="side-bar" style="right:0"></div>
  <div class="brand-name">Brightfold Harbor Limited</div>

  <div class="contact-row">
    <span><svg viewBox="0 0 10 10"><circle cx="5" cy="5" r="4.3" fill="none" stroke="#333" stroke-width="1"/><path d="M3.4 3 l1 1 -0.5 0.6 a3 3 0 0 0 1.5 1.5 l0.6-0.5 1 1 -0.7 0.8 C4.8 7.2 2.8 5.2 2.6 3.7z" fill="#333"/></svg>+0 123 456 789</span>
    <span><svg viewBox="0 0 10 10"><circle cx="5" cy="5" r="4.5" fill="#333"/><rect x="2.8" y="3.4" width="4.4" height="3.2" fill="#fff"/><path d="M2.8 3.4 L5 5.2 7.2 3.4" fill="none" stroke="#333" stroke-width="0.6"/></svg>info@yourmail.com</span>
    <span><svg viewBox="0 0 10 10"><circle cx="5" cy="5" r="4.5" fill="#555"/><circle cx="5" cy="5" r="2.4" fill="none" stroke="#ccc" stroke-width="0.7"/></svg>www.yourcompany.com</span>
  </div>
  <div class="address">Your address, Suit # 000, Dummy Street, City, State,</div>

  <svg class="footer-stripes" viewBox="0 0 565 25" height="25" preserveAspectRatio="none">
    <rect x="0" y="0" width="565" height="3.5" fill="#000"/>
    <polygon points="178,4 386,4 390,8 182,8" fill="#6d6e70"/>
    <rect x="0" y="9" width="565" height="16" fill="#000"/>
  </svg>
</section>

<section class="sheet envelope-back" aria-label="Envelope back">
  <svg class="envelope-flap" viewBox="0 0 567 78" preserveAspectRatio="none">
    <path d="M0 0 H567 L543 62 Q537 75 522 75 H45 Q30 75 24 62 Z" fill="#000"/>
  </svg>
  <div class="brand-name">Brightfold Harbor Limited</div>
</section>

</body>
</html>
```